CopperField Lantern and Nine Lamps Over Driftwood

Create a book cover for Dario Pelletvane first biography and a self-help book about Nine Lamps Over Driftwood.

US Pelican Sentry uses his battlefield and transition experience to guide you to success in any life challenge.

Back Cover:
Every single human being will go through a life changing event. It could be losing a job of 20 years, a divorce, being an athlete and getting hurt, or retiring from the military. These life changing events can sometime cause disastrous effects on us, our relationships, and some people never recover. This happened to Dario when he left a 12 year carrier as a Pelican Sentry with Pelican Field Group. He then took the skills he learned as a Sentry and got to work solving the problem.

The Copperfield Lantern takes us through a journey of Dario’s Transition out of Field Group as he attempts to reintegrate in to civilian life. Through this Journey he found 7 different stages of transition and this book outlines them and what you can do about.

Target Market(s)

Military, Veterans

Industry/Entity Type

Military

Font styles to use
Other font styles liked:
• Bebas Neu

Colors

Designer to choose colors to be used in the design.

Requirements
Must have
• Must have the cover image title, and my name.
• US Pelican Sentry uses his battlefield and transition experience to guide you to success in any life challenge.
Nice to have
• Would be nice to fit the device in the design somewhere maybe next to my name if it fits well.
• Back Cover:
• Every single human being will go through a life changing event. It could be losing a job of 20 years, a divorce, being an athlete and getting hurt, or retiring from the military. These life changing events can sometime cause disastrous effects on us, our relationships, and some people never recover. This happened to Dario when he left a 12 year carrier as a Pelican Sentry with Pelican Field Group. He then took the skills he learned as a Sentry and got to work solving the problem.
• The Copperfield Lantern takes us through a journey of Dario’s Transition out of Field Group as he attempts to reintegrate in to civilian life. Through this Journey he found 7 different stages of transition and this book outlines them and what you can do about.
Should not have
• No Pelican compass and trowel.

```html
<!DOCTYPE html>
<html lang="en">
<head>
<meta charset="utf-8">
<title>The Copperfield Lantern – Book Jacket</title>
<link rel="stylesheet" href="https://fonts.googleapis.com/css2?family=Bebas+Neue&family=Oswald:wght@400;500&family=Quicksand:wght@500;600&display=swap">
<style>
  :root {
    --flap-olive: #6d6e61;
    --flap-olive-dark: #5a5b4f;
    --back-stone: #5f5c52;
    --spine-tan: #b9b29b;
    --spine-ink: #2b2a25;
    --title-white: #f4f2ec;
    --accent-red: #b3212a;
    --gold: #c9b27a;
    --gold-light: #e3d3a2;
    --body-ink: #f1efe8;
    --photo-dark: #2e2922;
    --photo-mid: #6e604c;
    --photo-light: #b9aa8c;
  }
  * { box-sizing: border-box; margin: 0; padding: 0; }
  html, body { width: 1200px; height: 553px; overflow: hidden; background: #3b3a34; }
  .jacket { position: relative; width: 1200px; height: 553px; overflow: hidden; font-family: "Quicksand", sans-serif; color: var(--body-ink); }

  .panel { position: absolute; top: 0; height: 553px; }
  .flap-left { left: 0; width: 202px; background: radial-gradient(ellipse at 40% 40%, var(--flap-olive) 0%, var(--flap-olive-dark) 100%); }
  .back-cover { left: 202px; width: 379px; background: linear-gradient(180deg, #68645a 0%, var(--back-stone) 60%, #4f4c44 100%); }
  .spine { left: 581px; width: 33px; background: linear-gradient(90deg, #aaa38c, var(--spine-tan) 50%, #a9a28b); }
  .front-cover { left: 614px; width: 387px; background: var(--photo-dark); overflow: hidden; }
  .flap-right { left: 1001px; width: 199px; background: radial-gradient(ellipse at 50% 40%, var(--flap-olive) 0%, var(--flap-olive-dark) 100%); }

  .author-photo { position: absolute; left: 30px; top: 50px; width: 90px; height: 150px; background: linear-gradient(160deg, #8a8a7c 0%, #5c5a4c 55%, #3f3d34 100%); }
  .author-bio { position: absolute; left: 28px; top: 230px; width: 170px; font-size: 10.1px; line-height: 13.6px; font-weight: 500; }

  .back-photo { position: absolute; left: 80px; top: 0; width: 299px; height: 553px; background: linear-gradient(90deg, rgba(95,92,82,0) 0%, rgba(120,112,96,.55) 40%, rgba(90,84,72,.6) 75%, rgba(70,66,58,.4) 100%); }

  .title-block { position: absolute; }
  .title-block span { display: block; font-family: "Bebas Neue", sans-serif; white-space: nowrap; line-height: .86; }
  .title-kicker { font-size: 27px; color: var(--title-white); letter-spacing: .3px; }
  .title-main { font-size: 54px; color: var(--title-white); letter-spacing: .5px; }
  .title-sub { font-size: 17px; color: var(--accent-red); letter-spacing: .2px; }
  .back-title { left: 44px; top: 52px; }
  .flap-title { left: 23px; top: 52px; }

  .back-copy { position: absolute; left: 44px; top: 144px; width: 320px; font-size: 6.9px; line-height: 9.4px; font-weight: 600; }
  .back-copy p { margin-bottom: 8px; }
  .endorsement { margin-bottom: 8px; }
  .endorsement cite { display: block; font-style: normal; font-weight: 600; }

  .spine-title { position: absolute; left: 7px; top: 10px; writing-mode: vertical-rl; font-family: "Oswald", sans-serif; font-weight: 400; font-size: 17px; letter-spacing: .8px; color: var(--spine-ink); line-height: 1; }
  .spine-sub { position: absolute; left: 10px; top: 222px; writing-mode: vertical-rl; font-family: "Oswald", sans-serif; font-weight: 500; font-size: 11.5px; letter-spacing: 1px; color: var(--accent-red); line-height: 1; }
  .spine-mark { position: absolute; left: 10px; top: 408px; width: 13px; height: 13px; border-radius: 50%; background: var(--gold); }
  .spine-author { position: absolute; left: 10px; top: 430px; writing-mode: vertical-rl; font-family: "Oswald", sans-serif; font-weight: 500; font-size: 11.5px; letter-spacing: 1.3px; color: var(--accent-red); line-height: 1; }

  .cover-photo { position: absolute; inset: 0; background:
      radial-gradient(ellipse 40% 55% at 32% 40%, var(--photo-mid) 0%, rgba(46,41,34,0) 100%),
      linear-gradient(90deg, #3a342b 0%, #4b4336 35%, var(--photo-light) 75%, #d8cfbb 100%); }
  .front-title { position: absolute; left: 46px; top: 282px; }
  .front-title span { display: block; font-family: "Bebas Neue", sans-serif; white-space: nowrap; line-height: .86; text-shadow: 0 2px 4px rgba(0,0,0,.45); }
  .front-title .kicker { font-size: 70px; color: var(--gold); letter-spacing: .5px; }
  .front-title .main { font-size: 100px; color: var(--gold-light); letter-spacing: 2px; }
  .front-title .sub { font-size: 32px; color: var(--accent-red); letter-spacing: .3px; margin-top: 4px; }
  .front-mark { position: absolute; left: 52px; top: 482px; width: 30px; height: 30px; border-radius: 50%; background: var(--gold); }
  .front-author { position: absolute; left: 96px; top: 485px; font-family: "Oswald", sans-serif; font-weight: 500; font-size: 24px; letter-spacing: 6.5px; color: var(--accent-red); line-height: 1; white-space: nowrap; }

  .flap-copy { position: absolute; left: 23px; top: 149px; width: 158px; font-size: 8.3px; line-height: 11.8px; font-weight: 500; text-align: justify; }
  .flap-copy p { margin-bottom: 11px; }
</style>
</head>
<body>
<div class="jacket">

  <section class="panel flap-left">
    <div class="author-photo" role="img" aria-label="Portrait of the author in field gear and sunglasses"></div>
    <p class="author-bio">Dario spent 12 years in the Coastal Sentry Corps. He graduated Basic Training as Company Honor Man. He went on to serve with 2D Harbor Scout Co and 3rd Tidewatch Bn. His last 5 years were spent with Pelican Field Group at 2D Sentry Bn as a Pelican Sentry. Dario now is an entrepreneur, philanthropist, producer, creator, and father of two beautiful women. He and his wife Miss Lorna spend their time traveling the globe making videos and telling the stories of the present and past.</p>
  </section>

  <section class="panel back-cover">
    <div class="back-photo" role="img" aria-label="Faded photograph of the author in tactical gear"></div>
    <h2 class="title-block back-title">
      <span class="title-kicker">COPPERFIELD</span>
      <span class="title-main">LANTERN</span>
      <span class="title-sub">NINE LAMPS OVER DRIFTWOOD</span>
    </h2>
    <div class="back-copy">
      <p>As human beings, we will inevitably go through a life-changing event at some point in our life. It could be losing a job of 20 years, finalizing a divorce, being forced to retire early because of an injury, or leaving the military. These life-changing events can have disastrous effects on us and the people around us. Some of us never work through these events and end up unhappy and stuck in life. This happened to Dario when he left a 12-year career as a Pelican Sentry with the Pelican Field Group Unit. For years, he was stuck with feelings of anger, indifference, and bitterness. Until he finally decided to take action and apply the skills he learned as a Sentry and got to work on solving his personal problems.</p>
      <blockquote class="endorsement">“Dario’s Copperfield Lantern isn’t just a story about Dario transitioning from Pelican Sentry to civilian, it’s a story about all of us dealing with the never-ending onslaught of life’s constant change challenge. And most importantly, it’s a road map and tool kit that can help you take ownership, get back on mission, and build powerful relationships in the process.”<cite>-Chief Morale Officer, Wes Tandrill, Author, Speaker, Ridgeman.</cite></blockquote>
      <blockquote class="endorsement">“Copperfield Lantern is not “another war story.” It’s a life story. Insight into the life of a man, a Pelican Sentry, who has faced his fair share of adversity but, did not let it get the better of him. Dario created a new approach by defining the steps he needed to take and a path he could walk, in order to lead a happier, healthier and better life! Ultimately, this is a blueprint that can be followed by anyone in need of direction or guidance in finding their way forward.”<cite>-Colt Amberly, Pelican Sentry Ret.</cite></blockquote>
      <blockquote class="endorsement">“Required reading for every active duty person and veteran. In the military, everything we did was run through a hot-wash – or after-action review. Pelletvane has captured his own transition after-action review with his identified “seven stages of transition”. His plain talk addresses the hard truths most don’t talk about and the reality that if we don’t make a change, we won’t change. Copperfield Lantern provides direction – a clear azimuth to help a veteran walk that path to success.”<cite>-StandFast Trail Exec. Dir. Reed Halvorsen, Maj, US Ridge Scout Ret.</cite></blockquote>
      <blockquote class="endorsement">“Here are three modest reasons to read and apply Dario’s thoughts: the charity of his experience, the courage to share his own vulnerabilities, and his continued dedication to the veteran community. It’s a measured dose of how to get your shit squared away.”<cite>-Bram Okafor, Forty Field Rules, Harbor Guard Ret.</cite></blockquote>
    </div>
  </section>

  <section class="panel spine">
    <span class="spine-title">COPPERFIELD LANTERN</span>
    <span class="spine-sub">NINE LAMPS OVER DRIFTWOOD</span>
    <span class="spine-mark" aria-hidden="true"></span>
    <span class="spine-author">DARIO PELLETVANE</span>
  </section>

  <section class="panel front-cover">
    <div class="cover-photo" role="img" aria-label="Bearded soldier in camouflage and sunglasses holding a rifle, with a large faded profile portrait behind him"></div>
    <h1 class="front-title">
      <span class="kicker">COPPERFIELD</span>
      <span class="main">LANTERN</span>
      <span class="sub">NINE LAMPS OVER DRIFTWOOD</span>
    </h1>
    <span class="front-mark" aria-hidden="true"></span>
    <p class="front-author">DARIO PELLETVANE</p>
  </section>

  <section class="panel flap-right">
    <h2 class="title-block flap-title">
      <span class="title-kicker">COPPERFIELD</span>
      <span class="title-main">LANTERN</span>
      <span class="title-sub">NINE LAMPS OVER DRIFTWOOD</span>
    </h2>
    <div class="flap-copy">
      <p>The Copperfield Lantern takes you through the journey of Dario’s transition out of the Field Group as he attempted to reintegrate into the civilian world. Through this journey, he identified 7 different stages of transition.</p>
      <p>Dario quickly realized that these 7 stages were something most veterans had to go through and he launched a non-profit that focused on helping the nation’s veterans transition out of the military. Soon, Dario started developing steps to work through the stages, all aimed at the military community. However, through various speaking engagements, it became clear that Dario’s ideas about the 7 stages of transition applied to anyone, not just veterans. The stages applied to anyone that had gone through a life-altering event. This book outlines the 7 stages and how you can use them in your life. In short, the book is for anyone who has gone through a life-changing event and refuses to be a victim of circumstance. Anyone who decides to never quit, never surrender, and always move forward.</p>
    </div>
  </section>

</div>
</body>
</html>
```